Report Cover and Format For Company

Hello, I would like a report cover for my company and document format that will be used for reports, proposals and documents to customers.

Industry/Entity Type

Information Technology

```html
<!DOCTYPE html>
<html lang="en">
<head>
<meta charset="utf-8">
<title>Norvale Technology Group – Report Cover and Proposal Format</title>
<link rel="stylesheet" href="https://fonts.googleapis.com/css2?family=PT+Sans:wght@400;700&display=swap">
<style>
  :root {
    --bg-top: #5a5a5a;
    --bg-bottom: #262626;
    --cover-deep: #2a4f8f;
    --cover-light: #3f86c4;
    --brand-blue: #2c5d9e;
    --brand-teal: #3fa9d6;
    --ink: #222;
    --paper: #ffffff;
    --footer-ink: #3c78b8;
  }
  * { margin: 0; padding: 0; box-sizing: border-box; }
  html, body { width: 771px; height: 1200px; overflow: hidden; }
  body {
    position: relative;
    background: linear-gradient(180deg, var(--bg-top) 0%, #3a3a3a 35%, var(--bg-bottom) 100%);
    font-family: "PT Sans", Arial, sans-serif;
    color: var(--ink);
  }
  .sheet {
    position: absolute;
    width: 264px;
    height: 343px;
    box-shadow: 2px 3px 6px rgba(0,0,0,.55);
  }
  .cover {
    left: 230px; top: 60px;
    background:
      radial-gradient(ellipse 130px 150px at 110px 205px, rgba(120,180,230,.55), rgba(120,180,230,0) 100%),
      linear-gradient(160deg, var(--cover-deep) 0%, #2f66a8 55%, var(--cover-deep) 100%);
    color: #fff;
  }
  .cover-brand {
    position: absolute; right: 24px; top: 28px;
    text-align: right; font-weight: 700; font-size: 10px; line-height: 1.1;
  }
  .cover-url {
    position: absolute; left: 0; right: 0; bottom: 12px;
    text-align: center; font-size: 4.6px; font-weight: 700; letter-spacing: .2px;
  }
  .page { background: var(--paper); }
  .page-1 { left: 78px;  top: 433px; }
  .page-2 { left: 386px; top: 433px; }
  .page-3 { left: 78px;  top: 802px; }
  .page-4 { left: 386px; top: 802px; }
  .page-brand {
    position: absolute; right: 16px; top: 8px;
    display: flex; align-items: center; gap: 2px;
    font-weight: 700; font-size: 5px; color: var(--brand-blue);
  }
  .page-brand .dot { width: 6px; height: 6px; border-radius: 50%; background: var(--brand-blue); }
  .page-body {
    position: absolute; left: 28px; right: 30px; top: 38px;
    font-size: 4.7px; line-height: 6.9px; text-align: justify;
  }
  .page-1 .page-body { top: 57px; }
  .page-3 .page-body { top: 34px; }
  .page-4 .page-body { top: 36px; }
  .page-body p { margin-bottom: 6px; }
  .page-body h3 { font-size: 4.7px; font-weight: 700; margin: 6px 0 4px; }
  .page-body ul { list-style: none; margin-bottom: 6px; }
  .page-body li::before { content: "• "; }
  .indent { text-indent: 28px; }
  .signature { display: block; margin: 4px 0 10px; }
  .page-footer {
    position: absolute; left: 0; right: 0; bottom: 12px;
    text-align: center; font-size: 3.8px; line-height: 4.8px; color: var(--footer-ink);
  }
  .page-band {
    position: absolute; left: 0; right: 0; bottom: 0; height: 4px;
    background: linear-gradient(90deg, var(--brand-blue) 0 82%, var(--brand-teal) 82% 100%);
  }
  .fees { margin-top: 16px; }
</style>
</head>
<body>

<section class="sheet cover" aria-label="Report cover">
  <div class="cover-brand">NORVALE<br>TECHNOLOGY<br>GROUP</div>
  <div class="cover-url">www.norvaletech.net</div>
</section>

<section class="sheet page page-1" aria-label="Cover letter">
  <div class="page-brand"><span class="dot"></span>NORVALE</div>
  <div class="page-body">
    <p>October 18, 2016</p>
    <p>Lakeside Regional Council (LRC)<br>Attn: Peter Lindqvist, Information Technology Manager<br>410 Harbor Street, Suite 300<br>Millbrook, MO 64199</p>
    <p>Dear Mr. Lindqvist:</p>
    <p class="indent">Norvale Technology Group (Norvale) appreciates the opportunity to submit a proposal for consulting services. The Norvale team is highly competent and experienced in completing the scope of work required for the Information Technology Disaster Recovery Plan Review Consulting Services project.</p>
    <p class="indent">Norvale agrees with all terms, conditions, requirements and provisions included in the RFP, agrees to furnish all items upon which prices are offered at the price set opposite each item, and acknowledges all amendments. Norvale has an active registration in the SAM database and has entered all mandatory information and completed the Core, Assertions, and Representations and Certifications as well as the points of contact. Norvale's DUNS number is 00-000-0000.</p>
    <p>The contact information for persons authorized to negotiate on the offeror's behalf and sign the proposal are as follows:</p>
    <p>Dale Whitcombe, MS, CISSP<br>P.O. Box 518<br>Fairmont, VA 22990<br>(202) 555-0148<br>Thank you for considering Norvale's proposal.<br>Respectfully Submitted,</p>
    <svg class="signature" width="46" height="14" viewBox="0 0 46 14" aria-hidden="true"><path d="M2 12 L10 2 L9 12 L15 5 M13 9 L42 6" stroke="#222" stroke-width=".8" fill="none"/></svg>
    <p><b>Dale Whitcombe, member</b></p>
  </div>
  <div class="page-footer">P.O. Box 518, Fairmont, VA 22990<br>202.555.0148 | dwhitcombe@norvaletech.net | www.norvaletech.net</div>
  <div class="page-band"></div>
</section>

<section class="sheet page page-2" aria-label="Proposal page 1">
  <div class="page-brand"><span class="dot"></span>NORVALE</div>
  <div class="page-body">
    <h3>1.Identification of Information</h3>
    <ul>
      <li>Name of Key Contact Person: Dale Whitcombe, MS, CISSP</li>
      <li>Organization Name: Norvale Technology Group</li>
      <li>Address: P.O. Box 518, Fairmont, VA 22990</li>
      <li>Phone Number: (202) 555-0148</li>
      <li>Email Address: dwhitcombe@norvaletech.net</li>
    </ul>
    <h3>2.Background of the Individual and/or Organization Offering Consulting Services.</h3>
    <p>Norvale has the resources, knowledge, and experience to assist the LRC in obtaining an independent evaluation of the information security posture and to assist in the preparation of a disaster recovery plan that includes policy and procedures the LRC can implement. We have experience assessing federal standards for management, operational, and technical controls, including vulnerability scans of enterprise information systems and wide-area and local-area network infrastructure to assess the adequacy and effectiveness of the security controls that secure and safeguard sensitive data, databases, and files from unauthorized access, theft or modification, and that secure and safeguard software and hardware. Our team has performed federal information security audits at several federal departments, commissions and foundations. Norvale is currently supporting a federal Office of Inspector General, leading the annual Security Assessment and Authorizations of its sub agencies, working in a sub-contractor partnership with Harlow &amp; Birch, LLP.</p>
    <p>Norvale provides the following qualifications:</p>
    <ul>
      <li>A proven track record of success conducting HIPAA, A123, SOC-2 and FISMA audits;</li>
      <li>An organizational history of successful completion of similar projects;</li>
      <li>A cost-effective method for conducting assessments;</li>
      <li>Extensive experience documenting evidence to support the assessment;</li>
      <li>A staffing plan comprised of highly qualified IT security specialists with advanced degrees and industry certifications; and</li>
      <li>The ability to anticipate potential problems based on past experience and generate acceptable workarounds.</li>
    </ul>
  </div>
  <div class="page-footer">P.O. Box 518, Fairmont, VA 22990<br>202.555.0148 | dwhitcombe@norvaletech.net | www.norvaletech.net</div>
  <div class="page-band"></div>
</section>

<section class="sheet page page-3" aria-label="Proposal page 2">
  <div class="page-brand"><span class="dot"></span>NORVALE</div>
  <div class="page-body">
    <p>Dale Whitcombe is a founding member of Norvale Technology Group. He has 3 years' experience working with Norvale; 18 years' total experience working in the technical services industry. Dale is CISSP certified, holds a B.S. of Computer Information Systems, an M.S.A. for Information Resource Management, and a Post-Graduate Certificate for Information Security Management.</p>
    <p>Mr. Whitcombe has 18 years' experience as a federal employee supporting several federal departments and agencies. While at a defense agency, he was a key member of the Red Team supporting congressional-led exercises and more. He has overseen the FISMA compliance and authorizations of over 10 GSS and Major Applications. His development efforts have led to a data analytics tool projected to save the federal government over $10M in a 5-year span. He can easily identify strengths and weaknesses within an organization and implement policies, standards, and changes when needed in order to ensure maximum results.</p>
    <h3>3. Experience with Similar Engagements.</h3>
    <p>In the last 5 years, Norvale has conducted over 20 IT Security Audits. We are currently supporting a federal Office of Inspector General leading the IT Security Audits of all of its sub agencies over the next five years. Norvale is currently supporting a federal commission on its annual FISMA Security Audit. Norvale also has recently won an opportunity to support a federal CISO office here in Washington DC.</p>
    <h3>4. References for Similar Projects.</h3>
    <p><b>Reference 1:</b></p>
    <ul>
      <li>Federal Statistics Agency</li>
      <li>Anil Marwood</li>
      <li>Supervisory IT Specialist</li>
      <li>1200 Elm Hill Rd, Oakdale, MD 20999</li>
      <li>202-555-0173</li>
      <li>amarwood@example.net</li>
      <li>IT Security Audit of the Enterprise Content Management Systems</li>
      <li>June 2015 (8 months)</li>
      <li>All services were successfully completed and within budget</li>
    </ul>
  </div>
  <div class="page-footer">P.O. Box 518, Fairmont, VA 22990<br>202.555.0148 | dwhitcombe@norvaletech.net | www.norvaletech.net</div>
  <div class="page-band"></div>
</section>

<section class="sheet page page-4" aria-label="Proposal page 3">
  <div class="page-brand"><span class="dot"></span>NORVALE</div>
  <div class="page-body">
    <p><b>Reference 2:</b></p>
    <ul>
      <li>Federal Marine Science Administration</li>
      <li>Gerald Fenwick</li>
      <li>IT Security Lead</li>
      <li>800 East-West Hwy, Brookfield, MD 20999</li>
      <li>gerald.fenwick@example.gov</li>
      <li>Information System Security Officer for the Coastal Data Division</li>
      <li>2011–2013</li>
      <li>All services were successfully completed and within budget.</li>
    </ul>
    <p><b>Reference 3:</b></p>
    <ul>
      <li>Federal Development Foundation</li>
      <li>Teresa Olund</li>
      <li>Chief Information Security Officer</li>
      <li>900 J St NW #1000, Washington, DC 20099 Telephone tolund@example.gov</li>
      <li>FISMA Assessment and authorization of their hosted office suite implementation</li>
      <li>January 2016 – April 2016</li>
      <li>All services were successfully completed and within budget.</li>
    </ul>
    <h3>5. Detailed Project Plan.</h3>
    <p>[Provide a detailed project plan, outlining the tasks that will be completed along with the deliverable schedule. Include the estimated timeframe for the review and completion of written report.]</p>
    <h3>6. Proposed Hourly Fees and Total Project Fee.</h3>
    <p>[LRC has budgeted up to $10,000 for the scope of services. It is anticipated that the consultant should be able to complete the project within a 30- to 45-day timeframe. A consultant located outside the regional area may work remotely. Conference calls and online meeting technologies are acceptable and expected to contain costs.]</p>
    <p class="fees">Hourly Fee &nbsp;$<br>Total Project Fee &nbsp;$</p>
  </div>
  <div class="page-footer">P.O. Box 518, Fairmont, VA 22990<br>202.555.0148 | dwhitcombe@norvaletech.net | www.norvaletech.net</div>
  <div class="page-band"></div>
</section>

</body>
</html>
```